Food fans website needs a desktop homepage design

We need a desktop homepage design for TableHop.co.uk, a website to help you to find the best restaurants in each main city of Europe, with initial focus on London. It is not a directory with thousands of restaurants and reviews, else lists of top 20 restaurants for each area of the city. Food fans from all around the city will be able to keep an itinerary of where they eat, showing them later funny stats like "this month you really went for pizzas, don't you?". Keep it funny but professional.

A bit of branding has been done but this project give you total freedom to design the homepage of the site. The design must be a mix between minimal, flat and clean layout. The main idea is to keep it simple, easy to use and showing just the necessary elements.

For the font and colour scheme, we would like to use a thin but energetic font using the #E1393A colour as starting point even if you have freedom to slightly modify it. Blacks, greys and whites can be the secondary colours but we are open to introduce another main colour to the site like green, orange or yellow.

A simple wireframe has been attached to help you but the main elements that the page requires are the next:
- Panoramic fancy image in the header to contain the logo and the search form (the fields of the form are specified on the wireframe) and maybe some animated text to fill the right gap.
- List of results (10 results per page) showing the main info for each restaurant: name, thumbnail, location (zone, area), category, price, description, rating (no with stars please) and whatever you want to add that makes sense.
- Right hand sidebar with 3 widgets: Categories, Location and prices.

You can get the icons from glyphbarn.net.

We are open to have some text-shadows, rounded corners, box-shadows but trying to keep it minimal, flat and clean as much as possible. The main attractive of the site are the food/restaurant images.

Target Market(s)

22 - 45 food fans lovers from the city. busy people that want to disconnect and relax through the food. The don't mind to pay for quality and new experiences. Up to meet new places around them.

Industry/Entity Type

Restaurant

Requirements
Must have
• Panoramic image in the header, restaurants search form as per wireframe, list results with pagination, right hand sidebar with the widgets mention above and a nice footer with extra elements like "latest restaurants, latest tweets, etc.."
Nice to have
• This site will only be supported by the latest browsers so the idea is to have nice CSS3 transitions all around. Have that in mind at the time to design it even if you cannot show it on the design.
Should not have
• Busy backgrounds and unnecessary images that would slow down the page load.

```html
<!DOCTYPE html>
<html lang="en">
<head>
<meta charset="utf-8">
<title>TableHop in London</title>
<link rel="stylesheet" href="https://fonts.googleapis.com/css2?family=Libre+Baskerville:wght@400;700&family=Questrial&family=Arimo:ital,wght@0,400;0,700;1,400&display=swap">
<style>
:root{
  --orange:#fbb400;
  --orange-dark:#f29a00;
  --ink:#2b2b2b;
  --text:#6f6f6f;
  --muted:#9a9a9a;
  --line:#d9d9d9;
  --white:#ffffff;
  --page:#ffffff;
  --footer:#3d3d3d;
  --footer-text:#8a8a8a;
  --footer-rule:#555555;
  --page-btn:#b9b9b9;
}
*{margin:0;padding:0;box-sizing:border-box}
html,body{width:1200px;height:1051px;overflow:hidden;background:var(--page)}
body{position:relative;font-family:"Arimo",Arial,sans-serif;color:var(--text)}
.abs{position:absolute}

.hero{left:0;top:0;width:1200px;height:458px;
  background:radial-gradient(ellipse at 62% 45%,#f7e6d8 0,#c9412a 18%,transparent 40%),
  radial-gradient(ellipse at 20% 50%,#f08a1c 0,#d2400f 35%,#8e1408 70%),
  linear-gradient(90deg,#a51c0a,#e35a15 40%,#c23313 70%,#7a0f08)}
.logo{left:244px;top:28px;font-family:"Libre Baskerville",serif;font-weight:700;font-size:24px;color:#1e1a17;letter-spacing:-.3px}

.search{left:245px;top:99px;width:259px;height:350px;background:var(--white);padding:20px 14px 0 18px}
.search label{display:block;font-family:"Questrial",sans-serif;font-size:14.5px;color:#6b6b6b;height:18px;margin-bottom:7px;line-height:18px}
.field{width:227px;height:33px;border:1px solid #d6d6d6;font-family:"Arimo",sans-serif;font-style:italic;font-size:10.5px;color:#808080;padding:10px 0 0 8px;margin-bottom:8px;position:relative}
.field svg{position:absolute;right:10px;top:12px}
.search-btn{position:absolute;left:18px;top:296px;width:108px;height:34px;background:linear-gradient(#ffc21a,var(--orange-dark));color:var(--white);font-family:"Questrial",sans-serif;font-size:14.5px;text-align:center;line-height:34px;box-shadow:0 10px 8px -8px rgba(0,0,0,.25)}

.tagline{left:551px;top:137px;color:var(--white);font-family:"Libre Baskerville",serif}
.tagline h1{font-size:22.5px;font-weight:400;letter-spacing:.2px}
.tagline p{font-size:14px;margin-top:6px}
.tagline small{display:block;font-size:11.5px;font-weight:700;margin-top:32px}

.section-title{left:244px;top:492px;font-family:"Libre Baskerville",serif;font-weight:700;font-size:19px;color:var(--ink);letter-spacing:.3px}
.section-title span{color:var(--orange)}
.section-rule{left:244px;top:522px;width:535px;height:1px;background:var(--line)}

.result{left:245px;width:534px;height:175px}
.thumb{left:0;top:0;width:166px;height:122px;border:1px solid var(--line);padding:5px}
.thumb div{width:100%;height:100%;background:radial-gradient(circle at 40% 45%,#e23a1c 0,#f29a1e 30%,#7ea33b 55%,#d8d8d8 80%)}
.result h2{position:absolute;left:178px;top:8px;font-family:"Libre Baskerville",serif;font-size:15.5px;font-weight:700;color:var(--ink)}
.result p{position:absolute;left:178px;top:40px;width:338px;font-size:9.6px;line-height:13.6px;color:var(--text)}
.result .view{position:absolute;left:178px;top:110px;font-size:9px;font-weight:700;color:#666}
.meta{left:0;top:132px;width:534px;height:33px;border:1px solid var(--line);display:flex}
.meta .cell{width:41px;height:31px;border-right:1px solid var(--line);display:flex;align-items:center;justify-content:center}
.meta .stars{margin-left:auto;display:flex;gap:2px;align-items:center;padding-right:9px}

.pager{left:246px;top:905px;display:flex;gap:2px}
.pager span{width:27px;height:22px;background:var(--page-btn);color:#555;font-size:9.5px;text-align:center;line-height:22px}
.pager .current{background:var(--orange);color:var(--white)}

.widget{left:794px;width:201px}
.widget .icon{position:absolute;left:0;top:0;width:37px;height:34px;background:var(--orange);display:flex;align-items:center;justify-content:center}
.widget .bar{position:absolute;left:45px;top:0;width:156px;height:34px;background:var(--orange);color:var(--white);font-family:"Libre Baskerville",serif;font-weight:700;font-size:15px;line-height:34px;padding-left:11px;box-shadow:0 10px 8px -8px rgba(0,0,0,.2)}
.widget ul{position:absolute;left:45px;top:43px;list-style:none;width:200px}
.widget li{font-size:9.3px;color:#999;margin-bottom:11px;white-space:nowrap}
.widget li::before{content:"›";color:#555;font-size:12px;margin-right:4px}
.widget li a{color:#444;text-decoration:underline}

.footer{left:0;top:934px;width:1200px;height:117px;background:var(--footer)}
.footer h3{font-family:"Libre Baskerville",serif;font-weight:700;font-size:11.5px;color:#c9c9c9}
.footer h3 span{font-family:"Arimo",sans-serif;font-weight:400;font-size:9.5px;color:var(--footer-text)}
.links{left:245px;top:23px}
.links a{display:block;font-size:9.3px;color:var(--footer-text);text-decoration:underline;line-height:13.6px}
.links h3{margin-bottom:6px}
.divider{top:38px;width:1px;height:60px;background:var(--footer-rule)}
.about{left:424px;top:23px;width:330px}
.about p{font-size:9.3px;line-height:13.6px;color:var(--footer-text);margin-top:4px}
.about p em{font-style:normal;color:var(--orange)}
.copy{left:843px;top:56px;font-family:"Libre Baskerville",serif;font-weight:700;font-size:11.5px;color:#c9c9c9}
</style>
</head>
<body>

<header class="abs hero" role="img" aria-label="Close-up photograph of a berry and cream dessert"></header>
<div class="abs logo">TableHop in London</div>

<form class="abs search">
  <label>What restaurant ?</label>
  <div class="field">India<svg width="14" height="9" viewBox="0 0 14 9"><path d="M1 1l6 6 6-6" fill="none" stroke="#aaa" stroke-width="2.5"/></svg></div>
  <label>What kind of food ?</label>
  <div class="field">All</div>
  <label>Where ?</label>
  <div class="field">Everywhere</div>
  <label>Prices ?*</label>
  <div class="field">All</div>
  <div class="search-btn">Search</div>
</form>

<div class="abs tagline">
  <h1>Lorem Ipsum is simply dummy text</h1>
  <p>of the printing and typesetting industry</p>
  <small>Lorem Ipsum is simply dummy text</small>
</div>

<div class="abs section-title">BEST RESTAURANTS IN <span>LONDON</span></div>
<div class="abs section-rule"></div>

<article class="abs result" style="top:536px">
  <div class="abs thumb"><div role="img" aria-label="Photograph of assorted fresh fruit and vegetables"></div></div>
  <h2>Example 1</h2>
  <p>Lorem Ipsum is simply dummy text of the printing and typesetting industry. Lorem Ipsum has been the industry's standard dummy text ever since the 1500s, when an unknown rinter took a galley of type and scrambled it to make a type specimen book.</p>
  <span class="view">+ view</span>
  <div class="abs meta">
    <div class="cell"><svg width="18" height="18" viewBox="0 0 18 18" fill="#666"><circle cx="14" cy="3.5" r="2.6"/><circle cx="4" cy="9" r="2.6"/><circle cx="14" cy="14.5" r="2.6"/><path d="M14 3.5L4 9l10 5.5" stroke="#666" stroke-width="1.6" fill="none"/></svg></div>
    <div class="cell"><svg width="20" height="20" viewBox="0 0 20 20"><circle cx="10" cy="10" r="8.5" fill="none" stroke="#666" stroke-width="2"/><path d="M10 15.5c-2.5-3-3.5-4.5-3.5-6.3a3.5 3.5 0 017 0c0 1.8-1 3.3-3.5 6.3z" fill="#666"/><circle cx="10" cy="9" r="1.3" fill="#fff"/></svg></div>
    <div class="cell"><svg width="16" height="20" viewBox="0 0 16 20" fill="#666"><rect x="2" y="1" width="5" height="4"/><rect x="8" y="8" width="5" height="4"/><rect x="8" y="15" width="5" height="4"/><path d="M4.5 5v12H8M4.5 10H8" stroke="#666" stroke-width="1.6" fill="none"/></svg></div>
    <div class="cell"><svg width="14" height="18" viewBox="0 0 14 18"><path d="M11.5 4.5A3.6 3.6 0 005 5.5v10.5M1.5 9.5h8M1.5 16.5h11.5" fill="none" stroke="#666" stroke-width="2.4"/></svg></div>
    <div class="stars"><svg width="14" height="14" viewBox="0 0 24 24"><path d="M12 1l3.3 7 7.7.9-5.7 5.2 1.5 7.6L12 18l-6.8 3.7 1.5-7.6L1 8.9 8.7 8z" fill="#f7a600"/></svg><svg width="14" height="14" viewBox="0 0 24 24"><path d="M12 1l3.3 7 7.7.9-5.7 5.2 1.5 7.6L12 18l-6.8 3.7 1.5-7.6L1 8.9 8.7 8z" fill="#f7a600"/></svg></div>
  </div>
</article>

<article class="abs result" style="top:719px">
  <div class="abs thumb"><div role="img" aria-label="Photograph of assorted fresh fruit and vegetables"></div></div>
  <h2>Example 2</h2>
  <p>Lorem Ipsum is simply dummy text of the printing and typesetting industry. Lorem Ipsum has been the industry's standard dummy text ever since the 1500s, when an unknown rinter took a galley of type and scrambled it to make a type specimen book.</p>
  <span class="view">+ view</span>
  <div class="abs meta">
    <div class="cell"><svg width="18" height="18" viewBox="0 0 18 18" fill="#666"><circle cx="14" cy="3.5" r="2.6"/><circle cx="4" cy="9" r="2.6"/><circle cx="14" cy="14.5" r="2.6"/><path d="M14 3.5L4 9l10 5.5" stroke="#666" stroke-width="1.6" fill="none"/></svg></div>
    <div class="cell"><svg width="20" height="20" viewBox="0 0 20 20"><circle cx="10" cy="10" r="8.5" fill="none" stroke="#666" stroke-width="2"/><path d="M10 15.5c-2.5-3-3.5-4.5-3.5-6.3a3.5 3.5 0 017 0c0 1.8-1 3.3-3.5 6.3z" fill="#666"/><circle cx="10" cy="9" r="1.3" fill="#fff"/></svg></div>
    <div class="cell"><svg width="16" height="20" viewBox="0 0 16 20" fill="#666"><rect x="2" y="1" width="5" height="4"/><rect x="8" y="8" width="5" height="4"/><rect x="8" y="15" width="5" height="4"/><path d="M4.5 5v12H8M4.5 10H8" stroke="#666" stroke-width="1.6" fill="none"/></svg></div>
    <div class="cell"><svg width="14" height="18" viewBox="0 0 14 18"><path d="M11.5 4.5A3.6 3.6 0 005 5.5v10.5M1.5 9.5h8M1.5 16.5h11.5" fill="none" stroke="#666" stroke-width="2.4"/></svg></div>
    <div class="stars"><svg width="14" height="14" viewBox="0 0 24 24"><path d="M12 1l3.3 7 7.7.9-5.7 5.2 1.5 7.6L12 18l-6.8 3.7 1.5-7.6L1 8.9 8.7 8z" fill="#f7a600"/></svg><svg width="14" height="14" viewBox="0 0 24 24"><path d="M12 1l3.3 7 7.7.9-5.7 5.2 1.5 7.6L12 18l-6.8 3.7 1.5-7.6L1 8.9 8.7 8z" fill="#f7a600"/></svg><svg width="14" height="14" viewBox="0 0 24 24"><path d="M12 1l3.3 7 7.7.9-5.7 5.2 1.5 7.6L12 18l-6.8 3.7 1.5-7.6L1 8.9 8.7 8z" fill="#f7a600"/></svg></div>
  </div>
</article>

<nav class="abs pager"><span>&lt;&lt;</span><span class="current">1</span><span>2</span><span>3</span><span>&gt;&gt;</span></nav>

<aside class="abs widget" style="top:435px">
  <div class="icon"><svg width="24" height="24" viewBox="0 0 24 24" stroke="#fff" stroke-width="2.2" fill="none"><path d="M4 6l14 14M7 3l13 13M3 9l4-4"/></svg></div>
  <div class="bar">Categories</div>
  <ul><li><a>Italian restaurants</a> (2)</li><li><a>Italian restaurants</a> (2)</li></ul>
</aside>

<aside class="abs widget" style="top:589px">
  <div class="icon"><svg width="24" height="24" viewBox="0 0 20 20"><circle cx="10" cy="10" r="8.5" fill="none" stroke="#fff" stroke-width="1.8"/><path d="M10 15.5c-2.5-3-3.5-4.5-3.5-6.3a3.5 3.5 0 017 0c0 1.8-1 3.3-3.5 6.3z" fill="#fff"/><circle cx="10" cy="9" r="1.3" fill="#fbb400"/></svg></div>
  <div class="bar" style="padding-left:31px">Location</div>
  <ul><li><a>Restaurent in west london</a> (2)</li></ul>
</aside>

<aside class="abs widget" style="top:708px">
  <div class="icon"><svg width="16" height="20" viewBox="0 0 14 18"><path d="M11.5 4.5A3.6 3.6 0 005 5.5v10.5M1.5 9.5h8M1.5 16.5h11.5" fill="none" stroke="#fff" stroke-width="2.4"/></svg></div>
  <div class="bar" style="padding-left:31px">Prices</div>
  <ul><li><a>Casual restaurants(10-20)</a> (2)</li></ul>
</aside>

<footer class="abs footer">
  <div class="abs links">
    <h3>Basic Links</h3>
    <a>Lorem Ipsum is simply</a><a>Lorem Ipsum is simply</a><a>Lorem Ipsum is simply</a><a>Lorem Ipsum is simply</a>
  </div>
  <div class="abs divider" style="left:411px"></div>
  <div class="abs about">
    <h3>Basic Links <span>Lorem Ipsum is simply</span></h3>
    <p>Lorem Ipsum is simply dummy text of the printing and typesetting industry. Lorem Ipsum has <em>been the industry's standard dummy</em> text ever since the 1500s,</p>
  </div>
  <div class="abs divider" style="left:777px"></div>
  <div class="abs copy">TableHop London &copy; 2013</div>
</footer>

</body>
</html>
```